Belford & Company

We are a boutique commercial real estate firm. For our Business card design - sleek, modern, yet high-end/classy. Please see our website: belfordandcompany.example for details.

We currently need 2 business card names and the ability to add/change the business card information -
Name, Title, Address, Office #, Mobile #, Fax, Email and company website.

Industry/Entity Type

Real Estate

Contact Information for Business Card

Business card design - sleek, modern, yet high-end/classy. Please see our website: belfordandcompany.example for details.

Also, we'd like to have our slogan "Careful Work Sets The Standard." somewhere in there. We'd like to make some part of it raised or a different texture if possible.
Color #'s:
blue 19 36 128
light gray 222 222 221
dark gray 107 120 128

Also, we'd like to have our slogan "Careful Work Sets The Standard." somewhere in there. We'd like to make some part of it raised or a different texture if possible - grey on one side and blue on the other - rounded edges preferred. Maybe either metal/silver/grey raised logo on the back. Thank you!!

Requirements
Must have
• Sleek, modern, clean and classy design

```html
<!DOCTYPE html>
<html lang="en">
<head>
<meta charset="utf-8">
<title>Belford &amp; Company – Business Card</title>
<link rel="stylesheet" href="https://fonts.googleapis.com/css2?family=Lato:wght@400;700;900&family=Montserrat:wght@500;600&family=Roboto:wght@400&display=swap">
<style>
  :root {
    --page-bg: #e6e6e6;
    --navy: #131927;
    --white: #ffffff;
    --gold: #d4ae6a;
    --ink: #1e2230;
  }
  * { box-sizing: border-box; margin: 0; padding: 0; }
  html, body { width: 1200px; height: 1000px; overflow: hidden; }
  body { background: var(--page-bg); position: relative; font-family: "Roboto", sans-serif; }

  .card {
    position: absolute;
    left: 275px;
    width: 650px;
    height: 372px;
    background: var(--navy);
    box-shadow: 6px 10px 14px rgba(0,0,0,0.35);
    overflow: hidden;
  }
  .card--front { top: 85px; }
  .card--back { top: 549px; }

  .front__header {
    position: absolute; top: 0; left: 0; right: 0; height: 186px;
    display: flex; flex-direction: column; align-items: center; justify-content: center;
    padding-top: 14px;
  }
  .company-name {
    font-family: "Lato", sans-serif; font-weight: 900;
    color: var(--white); font-size: 29px; letter-spacing: -0.2px; line-height: 1;
  }
  .company-division {
    font-family: "Montserrat", sans-serif; font-weight: 600;
    color: var(--white); font-size: 15.5px; letter-spacing: 3px; margin-top: 3px;
  }

  .contact-band {
    position: absolute; top: 186px; left: 0; right: 0; height: 138px;
    background: var(--white);
  }
  .contact {
    position: absolute; display: flex; align-items: center; gap: 12px;
    color: var(--ink); font-size: 12px; text-transform: uppercase; line-height: 1.3;
  }
  .contact--phone { left: 57px; top: 14px; font-size: 14.5px; letter-spacing: 0.6px; }
  .contact--address { left: 349px; top: 14px; font-size: 11.5px; }
  .contact--email { left: 57px; top: 83px; font-size: 11.5px; }
  .contact--web { left: 349px; top: 83px; font-size: 11.5px; }
  .contact--web .contact__text { margin-left: 4px; }
  .icon {
    width: 40px; height: 41px; border-radius: 4px; background: var(--navy);
    display: flex; align-items: center; justify-content: center; flex-shrink: 0;
  }
  .icon svg { width: 24px; height: 24px; }

  .slogan {
    font-family: "Lato", sans-serif; font-weight: 700;
    color: var(--gold); text-transform: uppercase; white-space: nowrap;
  }
  .front__footer {
    position: absolute; top: 324px; left: 0; right: 0; bottom: 0;
    display: flex; align-items: center; justify-content: center;
  }
  .front__footer .slogan { font-size: 13px; letter-spacing: 2.6px; font-weight: 400; }

  .back__brand {
    position: absolute; left: 217px; top: 119px; width: 216px;
  }
  .back__lockup {
    display: flex; justify-content: space-between; align-items: flex-end;
    height: 100px; padding-bottom: 4px;
  }
  .back__mark { width: 84px; height: 92px; background: var(--gold); }
  .back__name {
    font-family: "Lato", sans-serif; font-weight: 900; color: var(--white);
    text-align: right; line-height: 1; text-transform: uppercase;
  }
  .back__name span { display: block; }
  .back__name .line-1 { font-size: 30px; }
  .back__name .line-2 { font-size: 21px; margin-top: 4px; }
  .back__brand .company-division {
    border-top: 2px solid var(--white); margin-top: 2px; padding-top: 2px;
    font-size: 14.5px; letter-spacing: 2.6px; text-align: center; white-space: nowrap;
  }
  .back__brand .slogan { font-size: 8.5px; letter-spacing: 1.3px; text-align: center; margin-top: 1px; }
</style>
</head>
<body>

<section class="card card--front" aria-label="Business card front">
  <header class="front__header">
    <h1 class="company-name">BELFORD &amp; COMPANY</h1>
    <p class="company-division">PROPERTY COUNSEL</p>
  </header>

  <div class="contact-band">
    <div class="contact contact--phone">
      <span class="icon"><svg viewBox="0 0 24 24"><path fill="#fff" d="M6.6 10.8a15.2 15.2 0 0 0 6.6 6.6l2.2-2.2c.3-.3.7-.4 1-.2 1.1.4 2.3.6 3.6.6.6 0 1 .4 1 1V20c0 .6-.4 1-1 1A17 17 0 0 1 3 4c0-.6.4-1 1-1h3.5c.6 0 1 .4 1 1 0 1.3.2 2.5.6 3.6.1.3 0 .7-.2 1z"/></svg></span>
      <span class="contact__text">555.014.2290</span>
    </div>
    <div class="contact contact--address">
      <span class="icon"><svg viewBox="0 0 24 24"><path fill="#fff" d="M12 2a7 7 0 0 0-7 7c0 5.2 7 13 7 13s7-7.8 7-13a7 7 0 0 0-7-7zm0 9.5A2.5 2.5 0 1 1 12 6.5a2.5 2.5 0 0 1 0 5z"/></svg></span>
      <span class="contact__text">2200 Harbor View Rd., Suite #310<br>Brookhaven, FL 32000</span>
    </div>
    <div class="contact contact--email">
      <span class="icon"><svg viewBox="0 0 24 24"><rect x="2" y="5" width="20" height="14" fill="#fff"/><path d="M2 5l10 8 10-8M2 19l7-6M22 19l-7-6" stroke="#131927" stroke-width="1" fill="none"/></svg></span>
      <span class="contact__text">info@belfordandcompany.example</span>
    </div>
    <div class="contact contact--web">
      <span class="icon"><svg viewBox="0 0 24 24" fill="none" stroke="#fff" stroke-width="1"><circle cx="12" cy="12" r="9.5"/><ellipse cx="12" cy="12" rx="4.5" ry="9.5"/><path d="M12 2.5v19M2.5 12h19M4 7h16M4 17h16"/></svg></span>
      <span class="contact__text">www.belfordandcompany.example</span>
    </div>
  </div>

  <footer class="front__footer">
    <p class="slogan">Careful Work Sets The Standard</p>
  </footer>
</section>

<section class="card card--back" aria-label="Business card back">
  <div class="back__brand">
    <div class="back__lockup">
      <span class="back__mark"></span>
      <h2 class="back__name"><span class="line-1">Belford</span><span class="line-2">&amp; Company</span></h2>
    </div>
    <p class="company-division">PROPERTY COUNSEL</p>
    <p class="slogan">Careful Work Sets The Standard</p>
  </div>
</section>

</body>
</html>
```